need professional, precise design for a website

I will start with a homepage design and if we pick your design, we'll have you design up to 6 more interior pages (we'll pay extra for these of course). We need a homepage design for a reserve study company based in Idaho, covering the northwest region. The company is called copper ridge capital study. Their current site is at https://www.copperridgecapital.example/ and they really like this site for inspiration https://www.fundplanhub.example/ but they would like an original design, just more modern and fresh like the sample site. I have logo files I will attach. They want something that looks financial and has a feel of accuity. Their main call to action will be to have someone fill in a contact form or call them on the phone. They will have a sample study that someone can download as on the fundplanhub site. You can use copy from their current site.

```html
<!DOCTYPE html>
<html lang="en">
<head>
<meta charset="utf-8">
<title>Copper Ridge Capital — Homepage</title>
<link rel="stylesheet" href="https://fonts.googleapis.com/css2?family=Montserrat:wght@400;500;600;700&family=Questrial&display=swap">
<style>
:root{
  --navy:#2d2a6e;
  --black:#111111;
  --orange:#f06a1d;
  --ink:#2a2a2a;
  --muted:#555555;
  --panel:#f5f5f5;
  --footer:#efefef;
  --white:#ffffff;
  --rule:#cfcfcf;
}
*{margin:0;padding:0;box-sizing:border-box}
html,body{width:670px;height:1200px;overflow:hidden;background:var(--white)}
body{position:relative;font-family:'Questrial',sans-serif;color:var(--ink)}
.abs{position:absolute}
a{color:inherit;text-decoration:none}

/* header */
.site-nav{top:0;left:0;width:670px;height:42px;background:var(--white)}
.nav-link{top:16px;font-family:'Montserrat',sans-serif;font-size:7.5px;letter-spacing:.3px;color:#333;text-transform:uppercase}
.nav-link.active{color:var(--navy)}
.brand{display:flex;align-items:center;gap:6px;font-family:'Montserrat',sans-serif;font-weight:500;color:var(--navy);white-space:nowrap}
.brand-dot{border-radius:50%;background:var(--navy);flex:none}
.brand-header{top:12px;left:279px;font-size:12px}
.brand-header .brand-dot{width:12px;height:12px}
.cta-bar{top:42px;left:0;width:670px;height:25px;display:flex}
.cta-bar a{display:flex;align-items:center;justify-content:center;color:var(--white);font-family:'Montserrat',sans-serif;font-weight:600;font-size:7.5px}
.cta-bar .quote{background:var(--navy);width:335px}
.cta-bar .specialist{background:var(--black);flex:1}

/* hero */
.hero{top:67px;left:0;width:670px;height:274px;background:linear-gradient(180deg,#7a6a5c 0%,#b98a5a 35%,#8a6a4c 65%,#3e3530 100%)}
.hero-shade{top:67px;left:0;width:300px;height:274px;background:linear-gradient(90deg,rgba(20,18,22,.55),rgba(20,18,22,0))}
.hero-title{top:152px;left:24px;font-family:'Montserrat',sans-serif;font-weight:700;font-size:17.5px;line-height:21px;color:var(--white);letter-spacing:.4px}
.hero-sub{top:200px;left:24px;font-family:'Montserrat',sans-serif;font-size:10.5px;line-height:16px;color:var(--white);letter-spacing:.3px}
.hero-dots{top:241px;left:27px}
.feature-strip{top:292px;left:62px;width:552px;height:44px;background:rgba(15,15,18,.78);display:flex}
.feature{flex:1;display:flex;align-items:center;gap:7px;padding-left:14px;color:var(--white);font-family:'Montserrat',sans-serif;font-size:7px;white-space:nowrap}
.feature.active{background:var(--navy);flex:0 0 127px;align-items:flex-start;padding-top:11px;padding-left:10px;position:relative}
.feature .more{position:absolute;left:80px;top:26px;color:var(--orange);font-size:5px}
.feature .dash{position:absolute;left:31px;top:29px;width:16px;height:1px;background:var(--white)}

/* intro */
.intro{top:341px;left:0;width:670px;height:299px;background:var(--panel)}
.brand-intro{top:368px;left:64px;font-size:15px}
.brand-intro .brand-dot{width:24px;height:24px}
.tagline{top:416px;left:64px;width:218px;height:21px;border-top:1px solid var(--rule);border-bottom:1px solid var(--rule);font-family:'Montserrat',sans-serif;font-size:9.2px;font-weight:500;line-height:19px;padding-left:3px;color:#111;white-space:nowrap}
.contact-row{top:448px;left:66px;font-family:'Montserrat',sans-serif;font-size:8px;color:#222;display:flex;gap:12px;white-space:nowrap}
.contact-row .sep{width:1px;height:11px;background:#444}
.intro-copy{top:381px;left:342px;width:272px;font-family:'Montserrat',sans-serif;font-size:8px;line-height:16px;color:#333}
.link-sm{font-size:5.5px;color:var(--navy);text-decoration:underline}
.intro-rule{top:477px;left:64px;width:544px;height:1px;background:var(--rule)}
.feature-list{top:498px;width:131px}
.list-head{display:flex;align-items:center;height:15px}
.list-head .brand-dot{width:14px;height:14px;border-radius:50%;background:var(--navy);margin-right:-3px;position:relative;z-index:1;border:2px solid var(--panel)}
.list-head span{background:var(--navy);color:var(--white);font-family:'Montserrat',sans-serif;font-size:8px;padding:2px 8px;flex:1;letter-spacing:.3px;white-space:nowrap}
.feature-list ul{list-style:none;margin-top:6px}
.feature-list li{font-family:'Montserrat',sans-serif;font-size:6.8px;height:18.3px;line-height:18px;border-bottom:1px dotted #cfcfcf;padding-left:10px;position:relative;color:#222}
.feature-list li::before{content:"›";position:absolute;left:1px;color:var(--orange);font-size:9px;line-height:17px}
.feature-list .link-sm{display:block;margin:9px 0 0 9px}
.sample-box{top:499px;left:389px;width:219px;height:113px;background:#1b1b1b}
.sample-text{top:506px;left:397px;width:125px;font-family:'Montserrat',sans-serif;font-size:8px;line-height:15px;color:var(--white)}
.sample-btn{top:562px;left:397px;width:108px;height:25px;border:1.5px solid var(--orange);color:var(--white);font-family:'Montserrat',sans-serif;font-size:6px;display:flex;align-items:center;justify-content:center}
.report{top:507px;left:525px;width:75px;height:96px;background:var(--white)}
.report-mark{top:4px;left:4px;font-family:'Montserrat',sans-serif;font-size:4px;color:#148a8c;display:flex;gap:3px;align-items:center}
.report-mark i{width:6px;height:6px;background:#148a8c;display:block}
.report-photo{top:17px;left:0;width:75px;height:56px;background:linear-gradient(180deg,#c8674d,#9a4a3a)}
.report-band{top:62px;left:0;width:75px;height:20px;background:#1c8a8b;color:var(--white);font-family:'Montserrat',sans-serif;font-size:4.5px;padding:3px 5px;line-height:6px}
.report-foot{top:82px;left:0;width:75px;height:14px;background:#333;color:#ddd;font-size:3.5px;padding:2px 4px;line-height:5px}

/* services */
.services-title{top:663px;left:0;width:670px;text-align:center;font-family:'Montserrat',sans-serif;font-weight:700;font-size:18px;letter-spacing:1.5px;color:var(--navy)}
.service-photo{top:708px;left:62px;width:266px;height:177px;background:linear-gradient(180deg,#9ab0bf 0%,#c9a581 45%,#b77a4e 70%,#4a3c36 100%);box-shadow:0 2px 6px rgba(0,0,0,.2)}
.service-heading{top:731px;left:341px;font-family:'Montserrat',sans-serif;font-weight:500;font-size:13px;letter-spacing:.4px;color:#111}
.service-copy{top:764px;left:341px;width:270px;font-family:'Montserrat',sans-serif;font-size:8px;line-height:16px;color:#333}
.service-btn{top:838px;left:341px;width:69px;height:18px;border:1.5px solid var(--orange);font-family:'Montserrat',sans-serif;font-size:6px;display:flex;align-items:center;justify-content:center}
.arrow-btn{top:788px;width:32px;height:22px;border:1px solid #333;background:var(--white);display:flex;align-items:center;justify-content:center}
.solid-btn{height:22px;display:flex;align-items:center;justify-content:center;color:var(--white);font-family:'Montserrat',sans-serif;font-weight:600;font-size:7.5px}
.all-services{top:912px;left:275px;width:120px;background:var(--navy)}

/* footer */
.site-footer{top:958px;left:0;width:670px;height:200px;background:var(--footer)}
.brand-footer{top:994px;left:240px;font-size:15px}
.brand-footer .brand-dot{width:24px;height:24px}
.footer-copy{top:1044px;left:90px;width:490px;text-align:center;font-size:8.3px;line-height:14px;color:#222}
.footer-links{top:1084px;left:0;width:670px;display:flex;justify-content:center;gap:14px;font-family:'Montserrat',sans-serif;font-size:7px;color:var(--navy)}
.footer-quote{top:1112px;left:239px;width:91px;height:18px;background:var(--navy);font-size:6px}
.footer-specialist{top:1112px;left:340px;width:91px;height:18px;background:var(--black);font-size:6px}
.copyright{top:1175px;left:0;width:670px;text-align:center;font-size:6.5px;color:#333}
</style>
</head>
<body>

<header class="abs site-nav">
  <a class="abs nav-link active" style="left:63px">Home</a>
  <a class="abs nav-link" style="left:124px">About Our Company</a>
  <div class="abs brand brand-header"><span class="brand-dot"></span>Copper Ridge Capital</div>
  <a class="abs nav-link" style="left:454px">Reserve Studies ▾</a>
  <a class="abs nav-link" style="left:560px">Contact Us</a>
</header>
<nav class="abs cta-bar">
  <a class="quote">Request a Quote</a>
  <a class="specialist">Contact Specialist</a>
</nav>

<section class="abs hero" role="img" aria-label="City skyline of high-rise towers at sunset"></section>
<div class="abs hero-shade"></div>
<h1 class="abs hero-title">HOA &amp; CONDOMINIUM<br>STUDIES</h1>
<p class="abs hero-sub">Every homeowners association is different.<br>Different sets of assets</p>
<svg class="abs hero-dots" width="56" height="10" viewBox="0 0 56 10">
  <line x1="4" y1="5" x2="50" y2="5" stroke="#fff" stroke-width="1"/>
  <circle cx="4" cy="5" r="3.5" fill="none" stroke="#fff"/><circle cx="4" cy="5" r="1.6" fill="#fff"/>
  <circle cx="28" cy="5" r="1.6" fill="#fff"/><circle cx="50" cy="5" r="1.6" fill="#fff"/>
</svg>
<div class="abs feature-strip">
  <div class="feature active">
    <svg width="18" height="18" viewBox="0 0 18 18" fill="none" stroke="#f06a1d" stroke-width="1.2"><rect x="2" y="2" width="12" height="14"/><polyline points="5,12 8,8 10,10 13,5"/></svg>
    <span>Finances &amp; Balances</span><i class="dash"></i><span class="more">Read More</span>
  </div>
  <div class="feature">
    <svg width="18" height="18" viewBox="0 0 18 18" fill="none" stroke="#f06a1d" stroke-width="1.2"><rect x="4" y="2" width="11" height="14"/><line x1="7" y1="6" x2="12" y2="6"/><line x1="7" y1="9" x2="12" y2="9"/><line x1="7" y1="12" x2="10" y2="12"/></svg>
    <span>HOA &amp; State Expertise</span>
  </div>
  <div class="feature">
    <svg width="18" height="18" viewBox="0 0 18 18" fill="none" stroke="#f06a1d" stroke-width="1.2"><rect x="3" y="3" width="12" height="9"/><line x1="6" y1="15" x2="12" y2="15"/><line x1="9" y1="12" x2="9" y2="15"/></svg>
    <span>The Finest Software</span>
  </div>
  <div class="feature">
    <svg width="18" height="18" viewBox="0 0 18 18" fill="none" stroke="#f06a1d" stroke-width="1.2"><rect x="4" y="4" width="10" height="12"/><line x1="2" y1="4" x2="16" y2="4"/><line x1="7" y1="8" x2="11" y2="8"/><line x1="7" y1="11" x2="11" y2="11"/></svg>
    <span>Decades in Building</span>
  </div>
</div>

<section class="abs intro"></section>
<div class="abs brand brand-intro"><span class="brand-dot"></span>Copper Ridge Capital</div>
<p class="abs tagline">Your financial road map for the next 30 years!</p>
<div class="abs contact-row"><span>(208) 555-0142</span><span class="sep"></span><span>Dana@CopperRidgeCapital.example</span></div>
<p class="abs intro-copy">A sound reserve plan is a steady guide that community boards have relied on for decades.&nbsp; Planning ahead is simply knowing the right points of origin and following the map that careful analysis has laid before us. <a class="link-sm">Read More</a></p>
<div class="abs intro-rule"></div>

<div class="abs feature-list" style="left:64px">
  <div class="list-head"><i class="brand-dot"></i><span>TOP TIER REPORTING</span></div>
  <ul><li>Expense Forecasting</li><li>Income Projections</li><li>Financial Mapping</li><li>Budget Planning</li></ul>
  <a class="link-sm">Read More</a>
</div>
<div class="abs feature-list" style="left:216px">
  <div class="list-head"><i class="brand-dot"></i><span>PRECISION &amp; FOCUS</span></div>
  <ul><li>Homeowners</li><li>Associations</li><li>Commercial Property</li><li>Common Area Assets</li></ul>
  <a class="link-sm">Read More</a>
</div>

<div class="abs sample-box"></div>
<p class="abs sample-text">Our report covers a one-year period and includes a 30-year cash flow forecast</p>
<a class="abs sample-btn">Read sample reserve study</a>
<div class="abs report">
  <div class="abs report-mark"><i></i>LEDGER POINT</div>
  <div class="abs report-photo" role="img" aria-label="Brick apartment building on the report cover"></div>
  <div class="abs report-band">PROPERTY NAME<br>Anywhere, USA</div>
  <div class="abs report-foot">Prepared for the Board</div>
</div>

<h2 class="abs services-title">SERVICES</h2>
<div class="abs service-photo" role="img" aria-label="City skyline at golden hour"></div>
<h3 class="abs service-heading">HOA RESERVES</h3>
<p class="abs service-copy">A sound reserve plan is a steady guide that community boards have relied on for decades.&nbsp; Planning ahead is simply knowing the right points of origin and following the map that careful analysis has laid before us.</p>
<a class="abs service-btn">Read more</a>
<a class="abs arrow-btn" style="left:23px" aria-label="Previous"><svg width="8" height="8" viewBox="0 0 8 8"><path d="M7 4H1M4 1L1 4l3 3" stroke="#111" stroke-width="1.4" fill="none"/></svg></a>
<a class="abs arrow-btn" style="left:614px" aria-label="Next"><svg width="8" height="8" viewBox="0 0 8 8"><path d="M1 4h6M4 1l3 3-3 3" stroke="#111" stroke-width="1.4" fill="none"/></svg></a>
<a class="abs solid-btn all-services">Read all Services</a>

<footer class="abs site-footer"></footer>
<div class="abs brand brand-footer"><span class="brand-dot"></span>Copper Ridge Capital</div>
<p class="abs footer-copy">A sound reserve plan is a steady guide that community boards have relied on for decades.&nbsp; Planning ahead is simply knowing the right points of origin and following the map that careful analysis has laid before us.</p>
<nav class="abs footer-links"><a>Home</a><a>About Our Company</a><a>Reserve Studies</a><a>Contact Us</a></nav>
<a class="abs solid-btn footer-quote">Request a Quote</a>
<a class="abs solid-btn footer-specialist">Contact Specialist</a>
<p class="abs copyright">Copyright Copper Ridge Capital, LLC © 2019 All Rights Reserved</p>

</body>
</html>
```